Willowmere Haven tri-fold brochure

We are a small assisted living in a home-like environment. Brochure should be warm, heartfelt and include the list of services we provide (see existing brochure). I also want the front picture replaced with stock photo (so no picture of owners). New name to use (instead of Hester) is Dorian Feltrowe, and email is feltrowe@quintmail.example. Address is same. If you can find better photos, that would be good, all the photos here are dated. We are looking for a more professional design that still conveys warmth, because we are in a home-setting and only care for 9 residents.

Target Market(s)

35-55 year old children looking for an assisted living because their parents are unable to care for them.

Industry/Entity Type

Environment

Contact Information for Business Card

Dorian Feltrowe
Willowmere Haven or Willowmere Haven Assisted Living
40718 Pinegrove Ln. Conroe, TX 77519
281-647-5192

Requirements
Must have
• List of services offered (feel free to re-word or add/change)
• Be sure to change "Hester/Hestie" to Dorian / Dorian Feltrowe

```html
<!DOCTYPE html>
<html lang="en">
<head>
<meta charset="utf-8">
<title>Willowmere Haven – Tri-fold Brochure</title>
<link rel="stylesheet" href="https://fonts.googleapis.com/css2?family=PT+Serif:wght@400;700&display=swap">
<style>
  :root {
    --page: #ffffff;
    --cream-top: #fffbe3;
    --cream-mid: #fcf3c6;
    --cream-low: #f8e9a6;
    --gold: #c2b43a;
    --gold-soft: #e7d98a;
    --ink: #1f1f1f;
    --accent-red: #c3141f;
    --logo-blue: #3c6fb4;
    --panel-edge: #3a3a3a;
    --photo-warm: #e2b878;
    --photo-deep: #8a5a3c;
  }
  * { margin: 0; padding: 0; box-sizing: border-box; }
  html, body { width: 1200px; height: 947px; overflow: hidden; background: var(--page); }
  body { position: relative; font-family: "PT Serif", Georgia, serif; color: var(--ink); font-weight: 700; }

  .panel {
    position: absolute; top: 28px; width: 374px; height: 894px;
    background: linear-gradient(180deg, var(--cream-top) 0%, var(--cream-mid) 55%, var(--cream-low) 100%);
    border: 1px solid var(--panel-edge);
    overflow: hidden;
  }
  .panel--why { left: 20px; }
  .panel--services { left: 415px; }
  .panel--home { left: 807px; }

  .rule { position: absolute; background: var(--gold); }
  .rule--top { top: 13px; left: 70px; right: 70px; height: 3px; }
  .rule--bottom { bottom: 13px; left: 70px; right: 70px; height: 3px; }
  .bar { position: absolute; width: 4px; background: var(--gold); }

  .flourish { position: absolute; width: 60px; height: 60px; background: radial-gradient(circle at 30% 30%, var(--gold-soft), transparent 70%); opacity: .7; }
  .flourish--tl { top: 6px; left: 6px; }
  .flourish--tr { top: 6px; right: 6px; }
  .flourish--bl { bottom: 6px; left: 6px; }
  .flourish--br { bottom: 6px; right: 6px; }

  .brand {
    position: absolute; top: 40px; left: 0; right: 0; text-align: center;
    font-size: 12px; font-weight: 400; color: var(--logo-blue); letter-spacing: .3px;
  }
  .brand::before {
    content: ""; display: inline-block; width: 9px; height: 9px; border-radius: 50%;
    background: var(--gold-soft); margin-right: 5px; vertical-align: 0;
  }

  .copy { position: absolute; left: 0; right: 0; text-align: center; }
  .copy span { display: block; white-space: nowrap; }

  .heading-why { top: 88px; font-size: 24px; line-height: 32px; }
  .intro { top: 138px; font-size: 17.5px; line-height: 29.5px; }
  .closing { top: 532px; font-size: 17.5px; line-height: 33.4px; }

  .heading-services { top: 68px; font-size: 40px; line-height: 48px; }
  .service-list { top: 116px; font-size: 14px; line-height: 25px; }
  .address { top: 788px; font-size: 17px; line-height: 24.5px; }

  .heading-home { top: 76px; font-size: 33px; line-height: 38px; }
  .home-copy { top: 162px; font-size: 17px; line-height: 29.4px; }
  .home-copy .left { text-align: left; padding-left: 20px; }
  .home-copy .highlight { color: var(--accent-red); }
  .contact { top: 838px; font-size: 13px; line-height: 18px; }

  .photo { position: absolute; }
  .photo--group { left: 35px; top: 296px; width: 308px; height: 220px;
    background: radial-gradient(ellipse at 50% 50%, var(--photo-warm) 40%, rgba(255,251,227,0) 75%), linear-gradient(135deg, var(--photo-deep), var(--photo-warm)); border-radius: 14px; }
  .photo--oval { left: 12px; top: 528px; width: 350px; height: 235px; border-radius: 50%;
    border: 5px solid #d4a165; background: linear-gradient(160deg, #9b7156 0%, #e9d4c2 50%, #7a3e5a 100%); }
  .photo--pets { left: 25px; top: 612px; width: 328px; height: 220px;
    border: 3px solid var(--gold); background: linear-gradient(150deg, #f6e5b0 0%, #d8a88a 50%, #f4ead8 100%); }
</style>
</head>
<body>

<section class="panel panel--why">
  <div class="flourish flourish--tl"></div><div class="flourish flourish--tr"></div>
  <div class="flourish flourish--bl"></div><div class="flourish flourish--br"></div>
  <div class="rule rule--top"></div><div class="rule rule--bottom"></div>
  <div class="bar" style="left:9px;top:97px;height:193px"></div>
  <div class="bar" style="right:9px;top:97px;height:193px"></div>
  <div class="bar" style="left:9px;top:532px;height:320px"></div>
  <div class="bar" style="right:9px;top:532px;height:320px"></div>
  <div class="brand">Willowmere Haven</div>
  <h1 class="copy heading-why"><span>Why Willowmere Haven?</span></h1>
  <p class="copy intro">
    <span>Choosing the right place</span>
    <span>For your loved one is an</span>
    <span>important decision. Willowmere</span>
    <span>Haven is here to help give you</span>
    <span>peace of mind.</span>
  </p>
  <div class="photo photo--group" role="img" aria-label="Photo of residents playing a table game together"></div>
  <p class="copy closing">
    <span>Innovative care in a residential</span>
    <span>environment provides a wonderful</span>
    <span>alternative to institutional living.</span>
    <span>Our residents truly become a</span>
    <span>family because of the small,</span>
    <span>intimate, home-like atmosphere.</span>
    <span>Our first concern is making life</span>
    <span>safe, comfortable and enjoyable</span>
    <span>for those who have been entrusted</span>
    <span>to us.</span>
  </p>
</section>

<section class="panel panel--services">
  <div class="flourish flourish--tl"></div><div class="flourish flourish--tr"></div>
  <div class="flourish flourish--bl"></div><div class="flourish flourish--br"></div>
  <div class="rule rule--top"></div><div class="rule rule--bottom"></div>
  <div class="bar" style="left:9px;top:97px;height:420px"></div>
  <div class="bar" style="right:9px;top:97px;height:420px"></div>
  <div class="brand">Willowmere Haven</div>
  <h1 class="copy heading-services"><span>Services</span></h1>
  <p class="copy service-list">
    <span>Medical supervision provided by visiting</span>
    <span>physicians and nursing personnel</span>
    <span>rehabilitation, home health and hospice</span>
    <span>services available through licensed</span>
    <span>professionals</span>
    <span>Medications and incontinence management</span>
    <span>Personal attention, caregiver involvement</span>
    <span>and heightened activities focusing on</span>
    <span>hobbies, crafts, exercise, music therapy,</span>
    <span>holiday and birthday celebrations, and plant</span>
    <span>and pet therapy.</span>
    <span>Nutritious home cooked meals and snacks</span>
    <span>with emphasis on hydration.</span>
    <span>Assistance with bathing, grooming and other</span>
    <span>personal needs including daily laundry and</span>
    <span>housekeeping.</span>
  </p>
  <div class="photo photo--oval" role="img" aria-label="Oval photo of three smiling residents at a table"></div>
  <address class="copy address" style="font-style:normal">
    <span>40718 Pinegrove Ln.</span>
    <span>Conroe, Texas 77519</span>
    <span>office@willowmerehaven.example</span>
  </address>
</section>

<section class="panel panel--home">
  <div class="flourish flourish--tl"></div><div class="flourish flourish--tr"></div>
  <div class="flourish flourish--bl"></div><div class="flourish flourish--br"></div>
  <div class="rule rule--top"></div><div class="rule rule--bottom"></div>
  <div class="bar" style="left:9px;top:97px;height:495px"></div>
  <div class="bar" style="right:9px;top:97px;height:495px"></div>
  <div class="brand">Willowmere Haven</div>
  <h1 class="copy heading-home"><span>Willowmere Haven</span><span>is your home</span></h1>
  <p class="copy home-copy">
    <span class="left">The comforts of home in a private</span>
    <span class="left">luxurious setting, allows loving</span>
    <span class="left">care with dignity</span>
    <span>Private or companion rooms,</span>
    <span>elegantly furnished or</span>
    <span>personalized to your style.</span>
    <span>A living room, family room, dining</span>
    <span>room, sunroom, and kitchen</span>
    <span>residents can call their own, so</span>
    <span class="highlight">they can live the way they always</span>
    <span class="highlight">have.</span>
    <span>Enjoy beautiful days on the patio</span>
    <span>and in the lovely garden area with</span>
    <span>beautiful trees, flowers, birds and</span>
    <span>pets.</span>
  </p>
  <div class="photo photo--pets" role="img" aria-label="Photo of two residents on a sofa with a dog and a parrot"></div>
  <p class="copy contact">
    <span>Dorian Feltrowe · 281-647-5192</span>
    <span>Email: feltrowe@quintmail.example</span>
  </p>
</section>

</body>
</html>
```